Presentation folder for holding wedding cake literature

We need to have a front cover design as well as a back cover design for a presentation folder to hold literature for a bakery who sells a lot of wedding cakes.

We have uploaded a couple copies of ideas that we like. They are for demonstrative purposes only.

The text on the front cover needs to be:
-The Sugar Atelier-
-Designing, baking and decorating perfect wedding cakes...Guaranteed!

On the back cover it needs to say:
-Serving VELVAsoft cakes and a "Silver Ribbon" Experience-

In addition the back cover must contain the "Silver Ribbon Baker" logo.

We will only supply photos if necessary. We would rather have you choose them.

We are open to any colors as long as they are soft.

For a reference of the client, go to http://www.brindlefieldsugaratelier.example

Target Market(s)

The target market is primarily women ages 25-40.

Industry/Entity Type

Wedding

Requirements
Must have
• Must have priorities are listed in the brief.
Nice to have
• Fonts should be a combination of "script" and one or more complementary styles.

Colors should be either a soft blue, pinkish tone or lavender tone. Mixing any of the colors with a light gray would be acceptable as well.
Should not have
• No dark colors such as black, red, purple, green or orange.

```html
<!DOCTYPE html>
<html lang="en">
<head>
<meta charset="utf-8">
<title>The Sugar Atelier – Presentation Folder</title>
<link rel="stylesheet" href="https://fonts.googleapis.com/css2?family=Quicksand:wght@400;500;700&family=Lobster&display=swap">
<style>
  :root {
    --paper: #ffffff;
    --blue-back: #5b9bc1;
    --blue-front: #5a92c4;
    --gold: #d4a033;
    --cream: #f7f3e3;
    --line: #eef4fa;
    --text-light: #ffffff;
    --tone-cake: #efe8d2;
    --tone-leaf: #c9d2b0;
    --tone-rose: #e2c4c2;
    --tone-pool: #9fcde6;
    --tone-linen: #ece9e4;
    --tone-lavender: #e3dcec;
  }
  * { box-sizing: border-box; margin: 0; padding: 0; }
  html, body { width: 1200px; height: 850px; overflow: hidden; background: var(--paper); }
  .canvas { position: relative; width: 1200px; height: 850px; overflow: hidden; font-family: "Quicksand", sans-serif; color: var(--text-light); }
  .cover { position: absolute; top: 20px; height: 818px; }
  .cover--back { left: 18px; width: 582px; background: var(--blue-back); }
  .cover--front { left: 600px; width: 582px; background: var(--blue-front); }
  .frame { position: absolute; inset: 0; width: 100%; height: 100%; }
  .abs { position: absolute; }

  .back-headline { left: 0; width: 564px; top: 232px; text-align: center; font-size: 29px; font-weight: 400; letter-spacing: -0.2px; }
  .back-headline strong { font-weight: 700; }
  .collage { left: 16px; top: 284px; width: 530px; height: 198px; background: var(--cream); }
  .swatch--gold { background: var(--gold); }
  .swatch--blue { background: var(--blue-back); }
  .photo--cake-leaves { background: radial-gradient(ellipse at 50% 65%, var(--tone-cake) 0%, var(--tone-cake) 40%, var(--tone-leaf) 100%); }
  .photo--cake-roses { background: radial-gradient(ellipse at 50% 60%, var(--tone-rose) 0%, #efe3df 55%, var(--tone-linen) 100%); }
  .photo--cake-pool { background: linear-gradient(180deg, var(--tone-pool) 0%, var(--tone-pool) 30%, var(--tone-cake) 75%, #ecd58e 100%); }
  .experience { left: 0; width: 564px; top: 494px; text-align: center; font-size: 23px; font-weight: 500; }
  .experience strong { font-weight: 700; }
  .brand-seal { left: 196px; top: 554px; width: 160px; height: 160px; border-radius: 50%; background: var(--paper); border: 5px solid var(--gold); display: flex; align-items: center; justify-content: center; text-align: center; }
  .brand-seal__name { font-weight: 700; font-size: 22px; line-height: 1.15; color: var(--gold); }

  .hero-mat { left: 87px; top: 130px; width: 406px; height: 276px; background: var(--cream); }
  .hero-photo { position: absolute; left: 11px; top: 12px; width: 382px; height: 253px; background: radial-gradient(ellipse at 72% 55%, #f6f3ec 0%, var(--tone-linen) 45%, var(--tone-lavender) 100%); }
  .banner { left: 64px; top: 442px; width: 454px; height: 86px; }
  .banner-title { left: 64px; top: 464px; width: 454px; text-align: center; font-family: "Lobster", cursive; font-size: 34px; color: var(--cream); }
  .tagline { left: 0; width: 582px; top: 575px; text-align: center; font-size: 19px; line-height: 26px; font-weight: 400; padding-left: 6px; }
  .tagline strong { font-weight: 700; }
</style>
</head>
<body>
<main class="canvas">

  <section class="cover cover--back" aria-label="Back cover">
    <svg class="frame" viewBox="0 0 582 818" aria-hidden="true">
      <g fill="none" stroke="var(--line)" stroke-width="1.3">
        <line x1="94" y1="30" x2="466" y2="30"/>
        <line x1="16" y1="136" x2="16" y2="284"/>
        <line x1="16" y1="482" x2="16" y2="676"/>
        <line x1="546" y1="136" x2="546" y2="284"/>
        <line x1="546" y1="482" x2="546" y2="676"/>
        <line x1="90" y1="790" x2="466" y2="790"/>
      </g>
    </svg>
    <p class="abs back-headline">Serving <strong>VELVAsoft</strong> cakes</p>
    <div class="abs collage">
      <div class="abs swatch--gold" style="left:12px;top:10px;width:77px;height:50px"></div>
      <div class="abs swatch--blue" style="left:100px;top:10px;width:88px;height:50px"></div>
      <div class="abs photo--cake-leaves" role="img" aria-label="Photo of a white tiered cake with green sugar leaves" style="left:12px;top:70px;width:176px;height:116px"></div>
      <div class="abs photo--cake-roses" role="img" aria-label="Photo of a couple cutting a cake topped with red roses" style="left:199px;top:13px;width:131px;height:173px"></div>
      <div class="abs photo--cake-pool" role="img" aria-label="Photo of a tiered cake with peach roses beside a pool" style="left:344px;top:13px;width:173px;height:115px"></div>
      <div class="abs swatch--blue" style="left:343px;top:134px;width:88px;height:51px"></div>
      <div class="abs swatch--gold" style="left:441px;top:134px;width:77px;height:51px"></div>
    </div>
    <p class="abs experience"><strong>“Silver Ribbon”</strong> Experience</p>
    <div class="abs brand-seal">
      <span class="brand-seal__name">Silver Ribbon<br>Baker</span>
    </div>
  </section>

  <section class="cover cover--front" aria-label="Front cover">
    <svg class="frame" viewBox="0 0 582 818" aria-hidden="true">
      <g fill="none" stroke="var(--line)" stroke-width="1.3">
        <line x1="108" y1="28" x2="480" y2="28"/>
        <line x1="30" y1="136" x2="30" y2="672"/>
        <line x1="560" y1="136" x2="560" y2="672"/>
        <line x1="108" y1="788" x2="480" y2="788"/>
      </g>
    </svg>
    <div class="abs hero-mat">
      <div class="hero-photo" role="img" aria-label="Photo of a couple cutting a white tiered wedding cake with lavender ribbons"></div>
    </div>
    <svg class="abs banner" viewBox="0 0 454 86" aria-hidden="true">
      <path d="M40 10 Q130 -4 230 12 Q330 28 420 6 L422 52 L454 76 Q410 82 372 70 Q300 88 228 72 Q140 56 58 72 Q28 80 0 72 L34 58 Z" fill="var(--gold)"/>
    </svg>
    <p class="abs banner-title">The Sugar Atelier</p>
    <p class="abs tagline">Designing, baking and decorating<br>perfect wedding cakes...<br><strong>Guaranteed!</strong></p>
  </section>

</main>
</body>
</html>
```